Allied Health team of Physiotherapists & Occupational Therapists seek a business card design

We have our new logo, we now need our new business cards and stationary. Willowmere: Oedema & Family Clinic is seeking a generic card design to represent our whole team and individual cards for each therapist that incorporates our new logo to communicate our holistic approach that is calming, nuturing, supportive and welcoming.
Our Physiotherapists and Occupational Therapists assess, treat and provide education for people who are at risk of or who have lymphoedema. This is often as a result of treatment for cancer. We provide pre-operative and post-operative management and cancer rehabilitation in our Pilates studio. Our team also consists of Physiotherapists who have a strong interest in pelvic floor and continence management for both men and women.

Target Market(s)

Mainly women health conscious

Industry/Entity Type

Allied Health: Physiotherapy / Occupational Therapy

Contact Information for Business Card

Address: 14 Tannerly Ave Frankston 3199 Phone: 84317756 fax: 8431 7759 Email: info@willowmerecareco.com.au Website: willowmerecareco.com.au Facebook address: facebook.com/WillowmereOedemaAndFamilyCareCentre. Room to write appointments. Individual cards need to have name, office email and individual email and professional details

Requirements
Must have
• Logo as per uploaded documents

```html
<!DOCTYPE html>
<html lang="en">
<head>
<meta charset="utf-8">
<title>Willowmere: Oedema &amp; Family Clinic – Business Card</title>
<link rel="stylesheet" href="https://fonts.googleapis.com/css2?family=Arimo:wght@400&display=swap">
<style>
  :root {
    --page-bg: #e6e4e1;
    --card-bg: #f5f3f0;
    --card-edge: #b9b7b4;
    --peach: #f6ad7b;
    --sage: #bfcac0;
    --ink: #353535;
    --divider: #5a5a5a;
  }
  * { margin: 0; padding: 0; box-sizing: border-box; }
  html, body {
    width: 1200px; height: 961px; overflow: hidden;
    background: var(--page-bg);
    font-family: "Arimo", Arial, sans-serif;
  }
  .business-card {
    position: absolute; left: 100px; top: 190px;
    width: 1000px; height: 580px;
    background: var(--card-bg);
    border: 1px dashed var(--card-edge);
    overflow: hidden;
  }
  .brand {
    position: absolute; left: 199px; top: 182px;
    width: 208px; height: 208px;
    display: flex; align-items: center; justify-content: center;
    text-align: center;
    color: var(--peach);
  }
  .brand-ring {
    position: absolute; inset: 0;
    border: 2px solid var(--peach); border-radius: 50%;
  }
  .brand-name { font-size: 22px; line-height: 1.3; font-weight: 400; }
  .divider {
    position: absolute; left: 501px; top: 165px;
    width: 1.5px; height: 250px; background: var(--divider);
  }
  .job-title {
    position: absolute; left: 543px; top: 172px;
    font-size: 34px; line-height: 1; font-weight: 400;
    color: var(--peach); letter-spacing: 0.3px;
  }
  .contact-list { position: absolute; left: 540px; top: 259px; list-style: none; }
  .contact-item {
    display: flex; align-items: center; gap: 11px;
    height: 28px; margin-bottom: 12px;
    font-size: 26px; line-height: 1; color: var(--ink);
  }
  .contact-icon { width: 24px; height: 24px; flex: none; }
  .address-bar {
    position: absolute; left: 0; top: 496px;
    width: 958px; height: 41px;
    background: var(--peach);
    display: flex; align-items: center; justify-content: center;
    padding-right: 20px;
    font-size: 16px; color: var(--ink);
  }
  .accent-square {
    position: absolute; left: 964px; top: 496px;
    width: 36px; height: 41px; background: var(--sage);
  }
</style>
</head>
<body>
  <section class="business-card">
    <div class="brand">
      <span class="brand-ring"></span>
      <span class="brand-name">Willowmere:<br>Oedema &amp;<br>Family Clinic</span>
    </div>

    <div class="divider"></div>

    <h1 class="job-title">YOUR TITLE</h1>

    <ul class="contact-list">
      <li class="contact-item">
        <svg class="contact-icon" viewBox="0 0 24 24" aria-hidden="true">
          <path fill="#f6ad7b" d="M6.6 3.5l2.6 3.6-1.7 2c.9 2.6 3 4.8 5.6 5.8l2-1.7 3.6 2.6-1.5 3.2c-7.4-.4-13.1-6.4-13.4-13.9z"/>
        </svg>
        <span>123 456 7890</span>
      </li>
      <li class="contact-item">
        <svg class="contact-icon" viewBox="0 0 24 24" aria-hidden="true">
          <rect x="7" y="2" width="10" height="20" rx="1.5" fill="none" stroke="#f6ad7b" stroke-width="1.6"/>
          <line x1="7" y1="18" x2="17" y2="18" stroke="#f6ad7b" stroke-width="1.2"/>
        </svg>
        <span>123 465 7890</span>
      </li>
      <li class="contact-item">
        <svg class="contact-icon" viewBox="0 0 24 24" aria-hidden="true">
          <rect x="1" y="6" width="22" height="14" fill="#f6ad7b"/>
          <path d="M1 6l11 8 11-8" fill="none" stroke="#f5f3f0" stroke-width="1.4"/>
        </svg>
        <span>hello@uremail.com</span>
      </li>
      <li class="contact-item">
        <svg class="contact-icon" viewBox="0 0 24 24" aria-hidden="true">
          <g fill="none" stroke="#f6ad7b" stroke-width="1.4">
            <circle cx="12" cy="12" r="10"/>
            <ellipse cx="12" cy="12" rx="4.5" ry="10"/>
            <line x1="2" y1="12" x2="22" y2="12"/>
            <line x1="3.5" y1="7" x2="20.5" y2="7"/>
            <line x1="3.5" y1="17" x2="20.5" y2="17"/>
          </g>
        </svg>
        <span>www.urwebsite.com</span>
      </li>
    </ul>

    <div class="address-bar">786 Fennimore Ln Calderwood, OR, US</div>
    <div class="accent-square"></div>
  </section>
</body>
</html>
```